KLD Photography Editing & Support Services for Real Estate

We require a double sided A4 flyer to promote our photography services to real estate agencies.
This particular service is targeted to rural areas where reliable, professional and highly skilled photographers are difficult to source. We teach the agent how to photograph, they upload files to a server and we take care of the rest (image editing, quality control and delivery). This will give the agents flexibility with when to shoot and eliminates the stress of managing a photographer / contractor. We offer a 1 day face to face training session and competitive packages for equipment start up.
We would like the flyer to look clean & very professional. The flyer should showcase samples of our work to highlight what can be achieved by using our services. We like the look of a black or dark background behind the text and feel that would look nice with our photographs provided. Otherwise open to your suggestions and ideas.
TEXT FOR FLYER:
Welcome to the KLD Real Estate Photography Editing and Support Service
• Take your real estate business to the next level by providing impressive real estate imagery that makes you stands out from the competition
• Omit the stress of trying to find a good photographer or managing an unreliable one and hence have more time to focus on other aspects of your business
• Showcase your listings with better quality and more impactful photographs than your competitors thereby increasing potential for a quick sale
• Great first impressions matter and you will achieve this by looking and feeling more professional. This will attract and retain more future clients.
HOW IT WORKS
• We understand that your time is valuable, so let us handle the editing and delivery of your images. You shoot, and we take care of the rest.
• Images are edited and delivered within 1 working day
INCLUSIONS:
• Full day face to face training (we come to you) and instructional handbook
• We will teach you everything you need to know about your equipment and how to take stunning real estate photographs
• Service turnaround within 1 working day
• Free HELP desk service Mon-Fri
• 12 month Exclusivity (rural towns only) for a limited time
INVESTMENT
• 99 per listing for us to manage images including editing, quality control and delivery (10 Images)
• Ask us about competitive packages for photography equipment if required
SUMMARY
The KLD Real Estate Photography Editing and Support Service is the perfect solution for busy real estate professionals who want to take their business to the next level. Our service is affordable, flexible, and designed to help you showcase your listings in the best possible light.
Contact us today to learn more about how we can help you.

```html
<!DOCTYPE html>
<html lang="en">
<head>
<meta charset="utf-8">
<title>KLD Real Estate Photography Flyer</title>
<link href="https://fonts.googleapis.com/css2?family=Cinzel:wght@400;500&family=Montserrat:wght@300;400;500;600;700&display=swap" rel="stylesheet">
<style>
:root{
  --bg:#ffffff;
  --paper:#ffffff;
  --panel:#333b40;
  --light:#eceeed;
  --ink:#2b3236;
  --white:#ffffff;
  --frame:rgba(255,255,255,.75);
}
*{box-sizing:border-box;margin:0;padding:0}
html,body{width:1200px;height:799px;overflow:hidden;background:var(--bg);font-family:"Montserrat",sans-serif;color:var(--ink)}
.page{position:absolute;top:94px;width:436px;height:615px;background:var(--paper)}
.page--front{left:124px}
.page--back{left:654px;width:430px}
.abs{position:absolute}
.light-band{position:absolute;background:var(--light)}
.photo{position:absolute}
.photo.framed::after{content:"";position:absolute;inset:8px;border:1px solid var(--frame)}
.panel{position:absolute;background:var(--panel);color:var(--white)}
.ticks{list-style:none}
.ticks li{position:relative;padding-left:18px;font-size:6.3px;line-height:1.45;margin-bottom:7px;text-align:justify}
.ticks li svg{position:absolute;left:0;top:1px;width:7px;height:7px}
.welcome-title{font-family:"Cinzel",serif;font-size:24px;text-align:center;letter-spacing:1px;margin-top:14px}
.welcome-sub{font-size:11.4px;font-weight:300;text-align:center;line-height:1.4;margin:6px 0 15px}
.wordmark{position:absolute;display:flex;align-items:center;gap:6px;font-family:"Montserrat",sans-serif;font-weight:600;color:var(--ink);white-space:nowrap}
.wordmark-dot{display:block;background:var(--ink)}
.h-works{font-size:11px;font-weight:700;letter-spacing:.2px}
.contact-lead{font-size:8.2px;line-height:1.5}
.contact-lead b{font-weight:700}
.contact-mail{font-size:11.5px;display:flex;align-items:center;gap:6px}
.contact-phone{font-size:22px;font-weight:700;display:flex;align-items:center;gap:6px}
.panel-head{font-size:10.4px;font-weight:700;text-align:center;letter-spacing:.3px}
.summary-head{font-size:10.5px;font-weight:700}
.summary-text{font-size:6.4px;line-height:1.5;text-align:justify}
.footer-line{font-size:7.4px;text-align:center;width:100%}
.footer-line b{font-weight:700}
</style>
</head>
<body>

<section class="page page--front">
  <div class="photo" role="img" aria-label="Dark timber country house at dusk with garden path" style="left:13px;top:9px;width:410px;height:223px;background:linear-gradient(180deg,#8aa2c1 0%,#c9b9a6 30%,#3c3d3c 55%,#4f6a3a 85%,#6b7a4c 100%)"></div>
  <div class="wordmark" style="right:38px;top:30px;font-size:11px">
    <span class="wordmark-dot" style="width:7px;height:7px"></span>Kara Lindell
  </div>
  <div class="light-band" style="left:13px;top:232px;width:410px;height:370px"></div>

  <div class="panel" style="left:23px;top:200px;width:192px;height:304px;padding:0 15px">
    <div class="welcome-title">WELCOME</div>
    <div class="welcome-sub">To The KLD<br>Real Estate Photography<br>Editing And Support Service</div>
    <ul class="ticks">
      <li><svg viewBox="0 0 10 10"><circle cx="5" cy="5" r="5" fill="#fff"/><path d="M2.6 5.2l1.7 1.6 3.2-3.4" stroke="#333b40" stroke-width="1.4" fill="none"/></svg>Take your real estate business to the next level by providing impressive real estate imagery that makes you stands out from the competition</li>
      <li><svg viewBox="0 0 10 10"><circle cx="5" cy="5" r="5" fill="#fff"/><path d="M2.6 5.2l1.7 1.6 3.2-3.4" stroke="#333b40" stroke-width="1.4" fill="none"/></svg>Omit the stress of trying to find a good photographer or managing an unreliable one and hence have more time to focus on other aspects of your business</li>
      <li><svg viewBox="0 0 10 10"><circle cx="5" cy="5" r="5" fill="#fff"/><path d="M2.6 5.2l1.7 1.6 3.2-3.4" stroke="#333b40" stroke-width="1.4" fill="none"/></svg>Showcase your listings with better quality and more impactful photographs than your competitors thereby increasing potential for a quick sale</li>
      <li><svg viewBox="0 0 10 10"><circle cx="5" cy="5" r="5" fill="#fff"/><path d="M2.6 5.2l1.7 1.6 3.2-3.4" stroke="#333b40" stroke-width="1.4" fill="none"/></svg>Great first impressions matter and you will achieve this by looking and feeling more professional. This will attract and retain more future clients.</li>
    </ul>
  </div>

  <div class="photo framed" role="img" aria-label="Dark living room with charcoal sofa and floor lamp" style="left:226px;top:200px;width:187px;height:147px;background:linear-gradient(135deg,#4a5258 0%,#6f767a 45%,#2d3236 100%)"></div>
  <div class="photo framed" role="img" aria-label="Bright open kitchen and dining area with timber beams" style="left:226px;top:356px;width:187px;height:148px;background:linear-gradient(180deg,#e9e6e1 0%,#d8d2c8 55%,#b99b78 100%)"></div>

  <div class="abs" style="left:34px;top:512px;width:168px">
    <div class="h-works">HOW IT WORKS</div>
    <ul class="ticks" style="margin-top:8px">
      <li style="font-size:6px;color:#4a5155"><svg viewBox="0 0 10 10"><circle cx="5" cy="5" r="5" fill="#333b40"/><path d="M2.6 5.2l1.7 1.6 3.2-3.4" stroke="#fff" stroke-width="1.4" fill="none"/></svg>We understand that your time is valuable, so let us handle the editing and delivery of your images. You shoot, and we take care of the rest.</li>
      <li style="font-size:6px;color:#4a5155"><svg viewBox="0 0 10 10"><circle cx="5" cy="5" r="5" fill="#333b40"/><path d="M2.6 5.2l1.7 1.6 3.2-3.4" stroke="#fff" stroke-width="1.4" fill="none"/></svg>Images are edited and delivered within 1 working day</li>
    </ul>
  </div>

  <div class="abs" style="left:226px;top:516px;width:190px">
    <div class="contact-lead"><b>Contact us today</b> to learn more about <b>how we can help you.</b></div>
    <div class="contact-mail" style="margin-top:12px"><svg width="13" height="13" viewBox="0 0 14 14"><circle cx="7" cy="7" r="6.3" fill="none" stroke="#2b3236" stroke-width=".9"/><rect x="3.8" y="4.8" width="6.4" height="4.4" fill="none" stroke="#2b3236" stroke-width=".8"/><path d="M3.8 4.8l3.2 2.4 3.2-2.4" fill="none" stroke="#2b3236" stroke-width=".8"/></svg><span>shoot@<b>karalindell</b>.com.au</span></div>
    <div class="contact-phone" style="margin-top:4px"><svg width="14" height="14" viewBox="0 0 24 24"><path d="M5 3l4 1 1.5 4.5-2.5 1.5a12 12 0 006 6l1.5-2.5L20 15l1 4-2 2C10 21 3 14 3 5z" fill="none" stroke="#2b3236" stroke-width="1.6"/></svg><span>61 400 555 018</span></div>
  </div>
</section>

<section class="page page--back">
  <div class="photo" role="img" aria-label="Cantilevered black cabin above a coastal cliff at sunset" style="left:12px;top:11px;width:411px;height:245px;background:linear-gradient(180deg,#8ba5c8 0%,#c9b7c4 35%,#e6c1a6 48%,#5f7fa0 55%,#3e5f7b 75%,#5b7a3e 100%)"></div>
  <div class="wordmark" style="right:38px;top:44px;font-size:18px;gap:8px">
    <span class="wordmark-dot" style="width:11px;height:11px"></span>Kara Lindell
  </div>
  <div class="light-band" style="left:12px;top:256px;width:411px;height:346px"></div>

  <div class="panel" style="left:27px;top:196px;width:193px;height:268px;padding:0 12px 0 12px">
    <div class="panel-head" style="margin-top:14px">INCLUSIONS:</div>
    <ul class="ticks" style="margin-top:10px">
      <li style="font-size:6.1px;padding-left:15px"><svg viewBox="0 0 10 10"><circle cx="5" cy="5" r="5" fill="#fff"/><path d="M2.6 5.2l1.7 1.6 3.2-3.4" stroke="#333b40" stroke-width="1.4" fill="none"/></svg>Full day face to face training (we come to you) and instructional handbook</li>
      <li style="font-size:6.1px;padding-left:15px"><svg viewBox="0 0 10 10"><circle cx="5" cy="5" r="5" fill="#fff"/><path d="M2.6 5.2l1.7 1.6 3.2-3.4" stroke="#333b40" stroke-width="1.4" fill="none"/></svg>We will teach you everything you need to know about your equipment and how to take stunning real estate photographs</li>
      <li style="font-size:6.1px;padding-left:15px"><svg viewBox="0 0 10 10"><circle cx="5" cy="5" r="5" fill="#fff"/><path d="M2.6 5.2l1.7 1.6 3.2-3.4" stroke="#333b40" stroke-width="1.4" fill="none"/></svg>Service turnaround within 1 working day</li>
      <li style="font-size:6.1px;padding-left:15px"><svg viewBox="0 0 10 10"><circle cx="5" cy="5" r="5" fill="#fff"/><path d="M2.6 5.2l1.7 1.6 3.2-3.4" stroke="#333b40" stroke-width="1.4" fill="none"/></svg>Free HELP desk service Mon-Fri</li>
      <li style="font-size:6.1px;padding-left:15px"><svg viewBox="0 0 10 10"><circle cx="5" cy="5" r="5" fill="#fff"/><path d="M2.6 5.2l1.7 1.6 3.2-3.4" stroke="#333b40" stroke-width="1.4" fill="none"/></svg>12 month Exclusivity (rural towns only) for a limited time</li>
    </ul>
    <div class="panel-head" style="margin-top:12px">INVESTMENT:</div>
    <ul class="ticks" style="margin-top:9px">
      <li style="font-size:6.1px;padding-left:15px"><svg viewBox="0 0 10 10"><circle cx="5" cy="5" r="5" fill="#fff"/><path d="M2.6 5.2l1.7 1.6 3.2-3.4" stroke="#333b40" stroke-width="1.4" fill="none"/></svg>99 per listing for us to manage images including editing, quality control and delivery (10 Images)</li>
      <li style="font-size:6.1px;padding-left:15px"><svg viewBox="0 0 10 10"><circle cx="5" cy="5" r="5" fill="#fff"/><path d="M2.6 5.2l1.7 1.6 3.2-3.4" stroke="#333b40" stroke-width="1.4" fill="none"/></svg>Ask us about competitive packages for photography equipment if required</li>
    </ul>
  </div>

  <div class="photo framed" role="img" aria-label="Warm timber lounge with tall windows at dusk" style="left:239px;top:196px;width:169px;height:180px;background:linear-gradient(180deg,#3e3b38 0%,#5a5f6e 35%,#9a7c5c 70%,#c9ad8c 100%)"></div>

  <div class="abs" style="left:239px;top:386px;width:170px">
    <div class="summary-head">SUMMARY:</div>
    <p class="summary-text" style="margin-top:4px">The KLD Real Estate Photography Editing and Support Service is the perfect solution for busy real estate professionals who want to take their business to the next level. Our service is affordable, flexible, and designed to help you showcase your listings in the best possible light.</p>
  </div>

  <div class="photo framed" role="img" aria-label="Modern farmhouse exterior at dusk" style="left:27px;top:475px;width:116px;height:90px;background:linear-gradient(180deg,#7f93b4 0%,#b9a393 45%,#6d6a5e 75%,#5e7045 100%)"></div>
  <div class="photo framed" role="img" aria-label="Bright bedroom with large windows" style="left:162px;top:475px;width:116px;height:90px;background:linear-gradient(135deg,#e3e4e3 0%,#bfc3c2 50%,#8d9a86 100%)"></div>
  <div class="photo framed" role="img" aria-label="Neutral bathroom with freestanding bath and timber vanity" style="left:296px;top:475px;width:117px;height:90px;background:linear-gradient(180deg,#d9d2c9 0%,#cfc5b9 60%,#b08c6a 100%)"></div>

  <div class="abs" style="left:12px;top:572px;width:411px">
    <div class="footer-line"><b>Contact us today</b> to learn more about <b>how we can help you.</b></div>
    <div class="footer-line" style="font-size:6.6px;margin-top:3px;display:flex;justify-content:center;align-items:center;gap:4px">
      <svg width="9" height="9" viewBox="0 0 14 14"><circle cx="7" cy="7" r="6.3" fill="none" stroke="#2b3236" stroke-width="1"/><rect x="3.8" y="4.8" width="6.4" height="4.4" fill="none" stroke="#2b3236" stroke-width=".9"/><path d="M3.8 4.8l3.2 2.4 3.2-2.4" fill="none" stroke="#2b3236" stroke-width=".9"/></svg>
      <span>shoot@<b>karalindell</b>.com.au &nbsp;|&nbsp;</span>
      <svg width="9" height="9" viewBox="0 0 14 14"><circle cx="7" cy="7" r="6.3" fill="none" stroke="#2b3236" stroke-width="1"/><path d="M4.5 4l1.6.4.6 1.7-1 .7a5 5 0 002.4 2.4l.7-1 1.7.6.4 1.6-.9.8C6.7 11 4 8.3 3.7 4.9z" fill="#2b3236"/></svg>
      <b>61 400 555 018</b>
    </div>
  </div>
</section>

</body>
</html>
```